Creation of a cover for the book "The Orchard Beyond Quiet Hills" with the painting "Vers lune.tif" enclosed; a romantic, sensual story of a young woman.
Size of the book: 14 x 20.5 cm
Title: "The Orchard Beyond Quiet Hills"
Author: "Maribel Soutan"
Publisher: "Harrow Editions" (at the bottom of the page).
Waiting for the author to be available
Waiting for the author to be available. Please apologize
general public
Book

```html
<!DOCTYPE html>
<html lang="en">
<head>
<meta charset="utf-8">
<title>The Orchard Beyond Quiet Hills — Cover</title>
<link rel="stylesheet" href="https://fonts.googleapis.com/css2?family=Bodoni+Moda:opsz,wght@6..96,400;6..96,500&family=Cormorant+Garamond:wght@500&display=swap">
<style>
  :root {
    --backdrop: #353535;
    --ink-light: #f4f1ec;
    --ink-frost: rgba(214, 232, 236, 0.88);
    --ink-teal: rgba(150, 205, 200, 0.9);
    --band: #141414;
    --paint-top: #8f8b92;
    --paint-mid: #5c6470;
    --paint-low: #2a2f36;
    --paint-base: #15181c;
    --paint-accent: #b3261e;
  }
  html, body {
    margin: 0;
    width: 1200px;
    height: 1200px;
    overflow: hidden;
    background: var(--backdrop);
  }
  .cover {
    position: absolute;
    left: 224px;
    top: 50px;
    width: 752px;
    height: 1100px;
    overflow: hidden;
    background: var(--paint-base);
  }
  .cover__painting {
    position: absolute;
    inset: 0 0 46px 0;
    background:
      radial-gradient(ellipse 30% 14% at 70% 24%, rgba(179, 38, 30, 0.75), rgba(179, 38, 30, 0) 100%),
      linear-gradient(175deg, var(--paint-top) 0%, var(--paint-mid) 38%, var(--paint-low) 70%, var(--paint-base) 100%);
  }
  .author {
    position: absolute;
    left: 18px;
    top: 36px;
    padding-left: 18px;
    border-left: 1.5px solid var(--ink-light);
    font-family: "Bodoni Moda", serif;
    font-weight: 400;
    font-size: 74px;
    line-height: 0.92;
    color: var(--ink-light);
    transform: scaleX(0.72);
    transform-origin: left top;
  }
  .title {
    position: absolute;
    left: 0;
    top: 0;
    margin: 0;
    font-family: "Bodoni Moda", serif;
    font-weight: 400;
  }
  .title__line {
    position: absolute;
    white-space: nowrap;
    line-height: 1;
    transform: scaleX(0.72);
    transform-origin: left top;
  }
  .title__line--a { left: 6px;   top: 440px; font-size: 118px; color: var(--ink-frost); }
  .title__line--b { left: 40px;  top: 540px; font-size: 250px; color: var(--ink-light); }
  .title__line--c { left: 110px; top: 800px; font-size: 118px; color: var(--ink-frost); }
  .title__line--d { left: 330px; top: 780px; font-size: 255px; color: var(--ink-teal); }
  .publisher {
    position: absolute;
    left: 0;
    right: 0;
    bottom: 0;
    height: 46px;
    background: var(--band);
    display: flex;
    align-items: center;
    justify-content: center;
    font-family: "Cormorant Garamond", serif;
    font-weight: 500;
    font-size: 28px;
    letter-spacing: 0.22em;
    color: var(--ink-light);
  }
</style>
</head>
<body>
  <div class="cover">
    <div class="cover__painting" role="img" aria-label="Cover painting in soft grey, blue and deep red tones"></div>
    <div class="author">Maribel<br>Soutan</div>
    <h1 class="title">
      <span class="title__line title__line--a">The Orchard</span>
      <span class="title__line title__line--b">Beyond</span>
      <span class="title__line title__line--c">Quiet</span>
      <span class="title__line title__line--d">Hills</span>
    </h1>
    <div class="publisher">HARROW&nbsp; EDITIONS</div>
  </div>
</body>
</html>
```